依頼詳細
タイ古式マッサージの看板ポスターを作成依頼をお願いします。
サイズはA2サイズです。よろしくお願いします。
例文は添付致します。
記載項目
店舗名、電話番号、ロゴ
希望イメージ
シンプル 複雑
単色 カラフル
暗い 明るい
日常 高級
遊び心 厳粛
未来的 伝統的
女性的 男性的
希望する色
赤系、茶系、緑系、グレー系
納品ファイル
• 高解像度JPG (.jpg)
• イラストレーター形式 (.ai)
補足説明
スタンド看板にしますのでA2サイズでなく原稿サイズ435x940でお願いします。
すみませんがよろしくお願いします。

色がとてもいいです!! パッと見て目立つしわかりやすいと思いました。
ありがとうございました。

この度は、皆様方にご提案頂きまして誠にありがとうございました。
また、何かございましたらよろしくお願いします。
ありがとうございました。

```html
<!DOCTYPE html>
<html lang="ja">
<head>
<meta charset="utf-8">
<title>タイ古式マッサージ</title>
<link rel="stylesheet" href="https://fonts.googleapis.com/css2?family=Noto+Serif+JP:wght@500;700;900&family=Shippori+Mincho+B1:wght@600;800&family=Cinzel:wght@500&display=swap">
<style>
:root{
  --bg-deep:#4a0608;
  --bg-mid:#7a1215;
  --bg-light:#9a1c1e;
  --wave:#3a0405;
  --panel:#2a0405;
  --gold-light:#fff2b8;
  --gold:#e9c56a;
  --gold-dark:#b98a2e;
  --white:#ffffff;
}
*{margin:0;padding:0;box-sizing:border-box}
html,body{width:1200px;height:2592px;overflow:hidden}
body{
  position:relative;
  font-family:"Noto Serif JP",serif;
  color:var(--white);
  background:radial-gradient(ellipse at 50% 40%,var(--bg-light) 0%,var(--bg-mid) 45%,var(--bg-deep) 100%);
}
.waves{position:absolute;left:0;top:0;width:1200px;height:2592px}
.lead{
  position:absolute;left:0;width:1200px;text-align:center;
  font-family:"Shippori Mincho B1",serif;font-weight:800;
  font-size:50px;line-height:80px;top:30px;letter-spacing:2px;
}
.gold{
  background:linear-gradient(180deg,var(--gold-light) 0%,var(--gold) 45%,var(--gold-dark) 100%);
  -webkit-background-clip:text;background-clip:text;color:transparent;
}
.title{
  position:absolute;left:0;width:1200px;text-align:center;
  font-family:"Noto Serif JP",serif;font-weight:900;
}
.title-1{top:200px;font-size:180px;letter-spacing:40px;line-height:220px;padding-left:40px}
.title-2{top:430px;font-size:190px;letter-spacing:10px;line-height:230px}
.voice{
  position:absolute;left:0;width:1200px;text-align:center;
  font-family:"Shippori Mincho B1",serif;font-weight:600;
  top:820px;font-size:38px;line-height:64px;
}
.voice .wide{font-size:36px}
.about{
  position:absolute;left:120px;top:1020px;width:960px;height:400px;
  background:var(--panel);border-radius:28px;
}
.about-art{
  position:absolute;left:350px;top:30px;width:260px;height:210px;
  border-radius:50%;
  background:radial-gradient(ellipse at center,#f4eeee 0%,#d8c8c8 55%,rgba(42,4,5,0) 72%);
}
.about-text{
  position:absolute;left:0;top:262px;width:960px;text-align:center;
  font-size:22px;line-height:25px;font-weight:500;
}
.price{position:absolute;left:160px;width:900px;height:160px}
.price-1{top:1480px}
.price-2{top:1680px}
.badge{
  position:absolute;left:20px;top:20px;width:124px;height:124px;border-radius:50%;
  background:linear-gradient(180deg,var(--gold-light),var(--gold) 50%,var(--gold-dark));
  color:var(--bg-mid);font-weight:900;font-size:44px;
  display:flex;align-items:center;justify-content:center;
}
.amount{
  position:absolute;left:175px;top:0;font-weight:700;font-size:150px;line-height:160px;letter-spacing:6px;
}
.tax{position:absolute;left:780px;top:78px;font-size:34px;font-weight:700;color:var(--gold)}
.closing{
  position:absolute;left:0;width:1200px;text-align:center;top:1920px;
  font-family:"Shippori Mincho B1",serif;font-weight:600;font-size:40px;line-height:80px;
}
.brand{
  position:absolute;left:0;width:1200px;top:2200px;text-align:center;
}
.brand-name{font-family:"Cinzel",serif;font-weight:500;font-size:110px;letter-spacing:10px;line-height:130px}
.brand-sub{font-family:"Cinzel",serif;font-weight:500;font-size:34px;letter-spacing:4px;margin-top:4px}
</style>
</head>
<body>
<svg class="waves" viewBox="0 0 1200 2592" aria-hidden="true">
  <path d="M0 560 C300 700 700 760 1200 600 L1200 680 C760 820 320 780 0 640 Z" fill="var(--wave)" opacity=".7"/>
  <path d="M0 650 C380 800 820 800 1200 690 L1200 740 C820 860 360 850 0 700 Z" fill="var(--wave)" opacity=".55"/>
  <path d="M0 2080 C360 2220 820 2200 1200 2060 L1200 2592 L0 2592 Z" fill="var(--wave)" opacity=".45"/>
</svg>

<div class="lead">デスクワークが多く、辛い首こりや肩こり<br>体の疲れがヒドイあなたに</div>

<div class="title title-1 gold">タイ古式</div>
<div class="title title-2 gold">マッサージ</div>

<div class="voice">
  『気づいたら、寝ていた』<br>
  『ビックリするほど、体が軽くなった』などの<br>
  <span class="wide">声をいただくタイ古式マッサージを体験してみませんか?</span>
</div>

<section class="about">
  <div class="about-art" role="img" aria-label="施術者が仰向けの人の脚を持ち上げてストレッチする白いシルエットのイラスト"></div>
  <p class="about-text">
    別名「二人で行うヨガ」と言われ、もみ、押すだけでなく<br>
    ストレッチ施術で血行を促しながら筋肉の柔軟性を高めていきます。<br>
    何だかプロレス技を掛けられているようなストレッチですが、<br>
    ゆっくりと体がほぐされていくので痛くなく、<br>
    「世界で一番気持ちいいマッサージ」と言われています。
  </p>
</section>

<div class="price price-1">
  <div class="badge">30分</div>
  <div class="amount gold">¥3,500</div>
  <div class="tax">(税込)</div>
</div>
<div class="price price-2">
  <div class="badge">60分</div>
  <div class="amount gold">¥5,900</div>
  <div class="tax">(税込)</div>
</div>

<div class="closing">全身をほぐしますので、<br>クイックマッサージにはない効果が実感できます。</div>

<div class="brand">
  <div class="brand-name">SERENA</div>
  <div class="brand-sub">Training studio</div>
</div>
</body>
</html>
```